Liebe Kreative
Es geht um ein Premium-Etikettendesign für einen Duftspray. Das Bild der Flasche werde ich Anhängen. Das sichtbare Etikett wird 7.2 x 10.8 cm gross sein. Das Etikett wird jedoch aufklappbar sein, d.h ein Teil wird auf den ersten Blick nicht sichtbar sein.
Die Mindestschriftgrösse ist Arial 7.
Das Design soll schlicht und Premium wirken. Wegbrise als Name sollte von oben nach unten geschrieben werden. Dieser Name sollte man hauptsächlich sehen, wenn man es von vorne betrachtet. Wichtig ist noch, dass beim sichtbaren Teil steht „Innenseite beachten“
Sichtbarer Teil:
Wegbrise (Produktname)
Inhalt: 30 ml
Gefahrenpiktogramme (Im Anhang. Auf Etikette 1x1cm gross)
Velmora GMBH
CH-8999 Musterwil
Tel. 022 555 73 48
Enthält / Contient: 2-Propanol
Wegbrise zweimal auf Kopfhöhe und 30cm vor dem Gesicht in die Luft sprühen und einatmen. Fördert die Konzentration und macht wach.
Innenseite beachten.
Nicht sichtbarer Teil:
ACHTUNG Kann Schläfrigkeit und Benommenheit verursachen Enthält D-Limonen, Citral. Kann allergische Reaktionen hervorrufen. Darf nicht in die Hände von Kindern gelangen.
ATTENTION Peut provoquer somnolence ou vertiges. Contient d-limonène, citral. Peut produire une réaction allergique. Tenir hors de portée des enfants.
Haltbarkeit: Nach dem Öffnen 6 Monate haltbar
Es ist wichtig, dass das ganze Stilvoll aussieht, es soll eine 'Premium-Ausstrahlung' haben.

```html
<!DOCTYPE html>
<html lang="de">
<head>
<meta charset="utf-8">
<title>Wegbrise – Etikett</title>
<link href="https://fonts.googleapis.com/css2?family=Montserrat:wght@400;500;600;700&family=Open+Sans:wght@400&display=swap" rel="stylesheet">
<style>
  :root {
    --plum: #3d1150;
    --gold: #d4b483;
    --gold-soft: rgba(212, 180, 131, 0.55);
    --caption: #9a9a9a;
    --paper: #ffffff;
    --haze: #f3f3f3;
  }
  * { box-sizing: border-box; margin: 0; padding: 0; }
  html, body {
    width: 857px; height: 1200px; overflow: hidden;
    background: var(--paper);
    font-family: "Montserrat", sans-serif;
  }
  .sheet { position: relative; width: 857px; height: 1200px; }
  .stage-band {
    position: absolute; left: 0; top: 0; width: 857px; height: 557px;
    background: linear-gradient(180deg, var(--haze) 0%, var(--paper) 10%, var(--paper) 88%, var(--haze) 100%);
  }
  .spec-caption {
    position: absolute; left: 29px; top: 587px;
    font-family: "Open Sans", sans-serif; font-size: 10px; letter-spacing: 0.12em;
    color: var(--caption);
  }
  .brand-title {
    position: absolute; left: 0; width: 857px; top: 657px; text-align: center;
    font-size: 28px; font-weight: 500; letter-spacing: 0.38em; padding-left: 0.38em;
    color: var(--gold);
  }
  .brand-tagline {
    position: absolute; left: 0; width: 857px; top: 700px; text-align: center;
    font-size: 11px; font-weight: 500; letter-spacing: 0.6em; padding-left: 0.6em;
    color: var(--gold);
  }

  .label {
    position: absolute; top: 785px; width: 309px; height: 308px;
    background: var(--plum); color: var(--gold); overflow: hidden;
    font-size: 7.6px; line-height: 9px;
  }
  .label--flat { left: 85px; }
  .label--fold { left: 462px; }
  .label b { font-weight: 700; }

  .label__notice { position: absolute; left: 10px; }
  .label--flat .notice-de { top: 10px; }
  .label--flat .notice-fr { top: 47px; }
  .label--flat .notice-shelf { top: 83px; }

  .hazard { position: absolute; width: 27px; height: 27px; }
  .label--flat .hazard--flame { left: 234px; top: 63px; }
  .label--flat .hazard--alert { left: 268px; top: 63px; }

  .fold-line--h { position: absolute; left: 0; right: 0; top: 102px; border-top: 1px dashed var(--gold-soft); }
  .fold-line--v { position: absolute; top: 0; bottom: 0; left: 103px; border-left: 1px dashed var(--gold-soft); }

  .maker-info { position: absolute; text-align: center; }
  .maker-info p + p { margin-top: 5px; }
  .label--flat .maker-info { left: 8px; right: 8px; top: 110px; }

  .label__brand {
    position: absolute; font-size: 27px; font-weight: 500; letter-spacing: 0.38em;
    line-height: 1;
  }
  .label--flat .label__brand { left: 0; right: 0; top: 209px; text-align: center; padding-left: 14px; }

  .volume { font-size: 9px; line-height: 1; position: absolute; }
  .label--flat .volume { left: 11px; top: 210px; writing-mode: vertical-rl; }

  .inside-note {
    position: absolute; font-size: 6.4px; letter-spacing: 0.25em; line-height: 1; font-weight: 500;
  }
  .label--flat .inside-note { left: 0; right: 0; bottom: 8px; text-align: center; }

  .corner-mark { position: absolute; width: 7px; height: 7px; }
  .label--flat .corner-mark { right: 3px; bottom: 3px; }
  .label--fold .corner-mark { right: 3px; top: 3px; }

  /* Fold label: text set bottom-to-top */
  .upward { position: absolute; writing-mode: vertical-rl; transform: rotate(180deg); }
  .label--fold .warnings { left: 10px; top: 10px; height: 288px; }
  .label--fold .warnings p + p { margin-block-start: 8px; }
  .label--fold .hazard--alert { left: 63px; top: 11px; transform: rotate(-90deg); }
  .label--fold .hazard--flame { left: 63px; top: 45px; transform: rotate(-90deg); }
  .label--fold .maker-info { left: 109px; top: 10px; height: 288px; }
  .label--fold .maker-info p + p { margin-top: 0; margin-block-start: 5px; }
  .label--fold .label__brand { left: 216px; top: 0; height: 298px; text-align: center; }
  .label--fold .volume { left: 209px; top: 286px; }
  .label--fold .inside-note { left: 294px; top: 0; height: 308px; text-align: center; }
</style>
</head>
<body>
<div class="sheet">
  <div class="stage-band"></div>

  <p class="spec-caption">ETIKETT 72 X 108 MM (108 X 108 MM)</p>
  <h1 class="brand-title">WEGBRISE</h1>
  <p class="brand-tagline">YOUR TAGLINE</p>

  <!-- Flat label view -->
  <section class="label label--flat">
    <p class="label__notice notice-de"><b>ACHTUNG:</b> Kann Schläfrigkeit und Benommenheit verursachen.<br>Enthält D-Limonen, Citral. Kann allergische Reaktionen hervorrufen.<br>Darf nicht in die Hände von Kindern gelangen.</p>
    <p class="label__notice notice-fr"><b>ATTENTION:</b> Peut provoquer somnolence ou vertiges.<br>Contient d-limonène, citral. Peut produire une réaction<br>allergique. Tenir hors de portée des enfants.</p>
    <p class="label__notice notice-shelf"><b>Haltbarkeit:</b> Nach dem Öffnen 6 Monate haltbar.</p>

    <svg class="hazard hazard--flame" viewBox="0 0 27 27" aria-label="Gefahrenpiktogramm entzündbar">
      <path d="M13.5 1.5 L25.5 13.5 L13.5 25.5 L1.5 13.5 Z" fill="none" stroke="var(--gold)" stroke-width="1.6"/>
      <path d="M13.6 7.5 C15.8 10.5 17 12.6 16.4 15.4 C15.9 17.6 14.2 18.6 13.4 18.6 C11.6 18.6 10.4 17.2 10.5 15.4 C10.6 13.8 11.8 12.8 12.2 11.6 C12.8 12.6 13 13.4 12.9 14.2 C14.1 12.6 14.2 10.2 13.6 7.5 Z" fill="var(--gold)"/>
      <rect x="10" y="19.4" width="7" height="1.2" fill="var(--gold)"/>
    </svg>
    <svg class="hazard hazard--alert" viewBox="0 0 27 27" aria-label="Gefahrenpiktogramm Achtung">
      <path d="M13.5 1.5 L25.5 13.5 L13.5 25.5 L1.5 13.5 Z" fill="none" stroke="var(--gold)" stroke-width="1.6"/>
      <rect x="12.3" y="7.5" width="2.4" height="8" rx="0.6" fill="var(--gold)"/>
      <circle cx="13.5" cy="18.3" r="1.4" fill="var(--gold)"/>
    </svg>

    <div class="fold-line--h"></div>

    <div class="maker-info">
      <p>Velmora GMBH · CH-8999 Musterwil · Tel. 022 555 73 48</p>
      <p><b>Enthält / Contient</b>: 2-Propanol</p>
      <p>Wegbrise zweimal auf Kopfhöhe und 30 cm vor dem Gesicht in die<br>Luft sprühen und einatmen. Fördert die Konzentration und macht wach.</p>
    </div>

    <p class="volume">℮ 30 ml</p>
    <p class="label__brand">WEGBRISE</p>
    <p class="inside-note">INNENSEITE BEACHTEN</p>
    <svg class="corner-mark" viewBox="0 0 7 7" aria-hidden="true"><path d="M7 0 V7 H0 Z" fill="var(--gold)"/></svg>
  </section>

  <!-- Fold-out label view -->
  <section class="label label--fold">
    <div class="upward warnings">
      <p><b>ACHTUNG:</b> Kann Schläfrigkeit und Benommenheit verursachen.<br>Enthält D-Limonen, Citral. Kann allergische Reaktionen hervorrufen.<br>Darf nicht in die Hände von Kindern gelangen.</p>
      <p><b>ATTENTION:</b> Peut provoquer somnolence ou vertiges.<br>Contient d-limonène, citral. Peut produire une réaction<br>allergique. Tenir hors de portée des enfants.</p>
      <p><b>Haltbarkeit:</b> Nach dem Öffnen 6 Monate haltbar.</p>
    </div>

    <svg class="hazard hazard--alert" viewBox="0 0 27 27" aria-label="Gefahrenpiktogramm Achtung">
      <path d="M13.5 1.5 L25.5 13.5 L13.5 25.5 L1.5 13.5 Z" fill="none" stroke="var(--gold)" stroke-width="1.6"/>
      <rect x="12.3" y="7.5" width="2.4" height="8" rx="0.6" fill="var(--gold)"/>
      <circle cx="13.5" cy="18.3" r="1.4" fill="var(--gold)"/>
    </svg>
    <svg class="hazard hazard--flame" viewBox="0 0 27 27" aria-label="Gefahrenpiktogramm entzündbar">
      <path d="M13.5 1.5 L25.5 13.5 L13.5 25.5 L1.5 13.5 Z" fill="none" stroke="var(--gold)" stroke-width="1.6"/>
      <path d="M13.6 7.5 C15.8 10.5 17 12.6 16.4 15.4 C15.9 17.6 14.2 18.6 13.4 18.6 C11.6 18.6 10.4 17.2 10.5 15.4 C10.6 13.8 11.8 12.8 12.2 11.6 C12.8 12.6 13 13.4 12.9 14.2 C14.1 12.6 14.2 10.2 13.6 7.5 Z" fill="var(--gold)"/>
      <rect x="10" y="19.4" width="7" height="1.2" fill="var(--gold)"/>
    </svg>

    <div class="fold-line--v"></div>

    <div class="upward maker-info">
      <p>Velmora GMBH · CH-8999 Musterwil · Tel. 022 555 73 48</p>
      <p><b>Enthält / Contient:</b> 2-Propanol</p>
      <p>Wegbrise zweimal auf Kopfhöhe und 30 cm vor dem Gesicht in die<br>Luft sprühen und einatmen. Fördert die Konzentration und macht wach.</p>
    </div>

    <p class="upward label__brand">WEGBRISE</p>
    <p class="volume">℮ 30 ml</p>
    <p class="upward inside-note">INNENSEITE BEACHTEN</p>
    <svg class="corner-mark" viewBox="0 0 7 7" aria-hidden="true"><path d="M0 0 H7 V7 Z" fill="var(--gold)"/></svg>
  </section>
</div>
</body>
</html>
```